Need a powerful, eye-catching book cover design for a Public Relations book for Lawyers.

We need a beautiful, elegant, and professional cover for a public relations book. We’ll be selling this both to (1) creative, experienced legal marketers, and (2) conservative lawyers. It must grab their attention visually, and have a bold, easy to read headline. The cover image may wrap around to the back cover.SIZE: 6 x 9” 100 pagesTITLE: The Ultimate Public Relations Handbook for LawyersSUBHEAD: Make millions using media and the InternetCO-AUTHORSRoss Fishman, JDJohn HellermanInclude a CALLOUT quote: “The definitive PR book. Simple and powerful.” – Hal Brisket, SkaddenGRAPHICS:You may use one of the attached photos, crop or flip them however you’d like, or use something else entirely. DESCRIPTION for the back cover:Why do some law firms have the best reputations or command the highest hourly rates? Why are some the go-to firms or thought leaders in particular specialties? Why are your competitors in the media more than you? Two words: Public relations. The co-authors are known worldwide as leaders in public relations, legal marketing, and branding. Mark Tolliver is called, “A PR Guru.” Bar Ledger magazine wrote ““Many people consider Dale Warbeck to be the nation’s foremost expert on law firm marketing.”Hal Brisket built Valmont into the first firm to generate $1 billion in revenue. Nadine Cortez is the nation’s go-to lawyer for women’s issues. Your home town’s top PI lawyer gets the first look at the biggest cases. Why? Strategic, intentional, effective PR. Are you tired of toiling in anonymity? Want to earn the attention of reporters and editors who can build your credentials and reputation for expertise? Wouldn’t it be nice to have more clients begging you to represent them because they heard you were the best in town? That is what public relations is designed to do. Want to get more respect, earn more clients, and charge higher rates? Get known as a thought leader in a specialty practice or industry? Public relations could be your most-important marketing tool. And this book will teach you precisely how. Ready to catapult your practice to new heights? Take a deep breath and dive in….

Target Market(s)

1. Creative marketing professionals
2. Conservative 40-year-old lawyers

Industry/Entity Type

Legal

Font styles to use
Serif

Requirements
Must have
• Want a simple, bold, eye catching design conveying professionalism and quality. This is a practical, how-to book. We need a simple design and strong headline that will work well at a small thumbnail size on Quiverly.
Nice to have
• Perhaps the microphone could wrap around the cover? A tight crop of a microphone that creates an abstract could work. Let's create something memorable.

```html
<!DOCTYPE html>
<html lang="en">
<head>
<meta charset="utf-8">
<title>The Complete Press Outreach Guidebook for Attorneys</title>
<link rel="stylesheet" href="https://fonts.googleapis.com/css2?family=Josefin+Sans:wght@300;400;600&family=Cormorant+Garamond:ital,wght@1,500&display=swap">
<style>
  :root {
    --page-bg: #ffffff;
    --stage-center: #3d2f78;
    --stage-mid: #1d1a3f;
    --stage-edge: #07070f;
    --spot-glow: rgba(255, 190, 130, 0.75);
    --spot-haze: rgba(255, 190, 130, 0);
    --mic-glow: rgba(120, 150, 230, 0.55);
    --mic-mid: rgba(70, 90, 170, 0.35);
    --mic-fade: rgba(40, 40, 90, 0);
    --silver-light: #f4f4f6;
    --silver-mid: #c9cacf;
    --silver-dark: #9ea0a7;
    --title-ink: #3b3c42;
    --cover-white: #ffffff;
    --cover-soft: #d9d9e2;
  }
  * { margin: 0; padding: 0; box-sizing: border-box; }
  html, body {
    width: 1200px;
    height: 800px;
    overflow: hidden;
    background: var(--page-bg);
  }
  .stage {
    width: 1200px;
    height: 800px;
    display: flex;
    align-items: center;
    justify-content: center;
  }
  .book-cover {
    position: relative;
    width: 480px;
    height: 720px;
    overflow: hidden;
    font-family: "Josefin Sans", sans-serif;
    color: var(--cover-white);
  }
  .cover-photo {
    position: absolute;
    inset: 0;
    background:
      radial-gradient(circle 34px at 40px 200px, var(--spot-glow) 0%, var(--spot-haze) 100%),
      radial-gradient(circle 40px at 410px 210px, var(--spot-glow) 0%, var(--spot-haze) 100%),
      radial-gradient(ellipse 70% 60% at 55% 45%, var(--stage-center) 0%, var(--stage-mid) 55%, var(--stage-edge) 100%);
  }
  .microphone-area {
    position: absolute;
    top: 260px;
    left: 150px;
    width: 320px;
    height: 460px;
    background:
      radial-gradient(ellipse 30% 16% at 28% 14%, var(--mic-glow) 0%, var(--mic-fade) 100%),
      linear-gradient(135deg, var(--mic-mid) 0%, var(--mic-fade) 75%);
  }
  .silver-banner {
    position: absolute;
    top: 0;
    left: 0;
    width: 480px;
    height: 180px;
  }
  .title-block {
    position: absolute;
    top: 34px;
    left: 0;
    width: 100%;
    text-align: center;
    color: var(--title-ink);
    font-weight: 400;
    font-size: 21px;
    line-height: 27px;
    letter-spacing: 0.5px;
    text-transform: uppercase;
  }
  .title-audience {
    position: absolute;
    top: 200px;
    left: 0;
    width: 100%;
    text-align: center;
    font-size: 24px;
    font-weight: 400;
    letter-spacing: 1px;
    text-transform: uppercase;
  }
  .subhead {
    position: absolute;
    top: 452px;
    left: 0;
    width: 100%;
    text-align: center;
    font-size: 14px;
    line-height: 18px;
    letter-spacing: 1.6px;
    text-transform: uppercase;
  }
  .authors {
    position: absolute;
    top: 508px;
    left: 40px;
    font-size: 11px;
    letter-spacing: 1.4px;
    color: var(--cover-soft);
    text-transform: uppercase;
  }
  .author-rule {
    position: absolute;
    top: 528px;
    left: 40px;
    width: 300px;
    border-top: 1px dashed var(--cover-soft);
  }
  .endorsement {
    position: absolute;
    top: 542px;
    left: 40px;
    width: 300px;
    text-align: center;
  }
  .endorsement-quote {
    font-family: "Cormorant Garamond", serif;
    font-style: italic;
    font-weight: 500;
    font-size: 16px;
    line-height: 19px;
  }
  .endorsement-source {
    margin-top: 3px;
    font-size: 8px;
    letter-spacing: 1.4px;
    color: var(--cover-soft);
    text-transform: uppercase;
  }
</style>
</head>
<body>
  <main class="stage">
    <section class="book-cover">
      <div class="cover-photo" role="img" aria-label="Dark stage backdrop in blue and purple with two warm spotlights"></div>
      <div class="microphone-area" role="img" aria-label="Close view of a stage microphone on its stand, angled down to the lower right"></div>

      <svg class="silver-banner" viewBox="0 0 480 180" aria-hidden="true">
        <defs>
          <linearGradient id="silverSheen" x1="0" y1="0" x2="1" y2="0">
            <stop offset="0" stop-color="#9ea0a7"/>
            <stop offset="0.5" stop-color="#f4f4f6"/>
            <stop offset="1" stop-color="#c9cacf"/>
          </linearGradient>
        </defs>
        <path d="M0 0 H480 V92 Q240 240 0 92 Z" fill="url(#silverSheen)"/>
        <path d="M0 92 Q240 240 480 92" fill="none" stroke="#ffffff" stroke-width="2"/>
      </svg>

      <h1 class="title-block">The Complete<br>Press Outreach<br>Guidebook</h1>
      <p class="title-audience">For Attorneys</p>

      <p class="subhead">Make millions using<br>media and the Internet</p>

      <p class="authors">Dale Warbeck, Mark Tolliver</p>
      <div class="author-rule"></div>

      <blockquote class="endorsement">
        <p class="endorsement-quote">“The definitive PR book. Simple and powerful.”</p>
        <p class="endorsement-source">– Hal Brisket, Valmont –</p>
      </blockquote>
    </section>
  </main>
</body>
</html>
```